Valdora necesita diseños de papeleria como tarjeta de presentacion, hoja membretada, sobres...

La papelería corporativa es para una tienda de moda multimarcas ubicada en Ecuador.
Los diseños tienen que ser de acuerdo a los diseños que adjunto.

```html
<!DOCTYPE html>
<html lang="es">
<head>
<meta charset="utf-8">
<title>Valdora – Tarjeta de presentación</title>
<link rel="stylesheet" href="https://fonts.googleapis.com/css2?family=Lato:wght@400;700;900&display=swap">
<style>
  :root {
    --backdrop: #2b2b2d;
    --card: #0b0c0e;
    --white: #ffffff;
    --red: #e3322b;
    --grey-text: #e8e8e8;
  }
  * { margin: 0; padding: 0; box-sizing: border-box; }
  html, body { width: 1200px; height: 970px; overflow: hidden; }
  body {
    background: var(--backdrop);
    font-family: "Lato", Arial, sans-serif;
    position: relative;
  }
  .card {
    position: absolute;
    width: 640px;
    height: 366px;
    background: var(--card);
    border-bottom: 6px solid var(--red);
    box-shadow: 0 14px 30px rgba(0,0,0,.55);
  }
  .card--front { left: 90px; top: 70px; }
  .card--back  { left: 470px; top: 530px; }

  .brand { position: absolute; color: var(--white); }
  .brand__name {
    font-weight: 900;
    letter-spacing: .22em;
    line-height: 1;
  }
  .brand__tagline {
    font-weight: 400;
    letter-spacing: .32em;
    margin-top: 8px;
  }
  .card--front .brand { left: 48px; top: 96px; }
  .card--front .brand__name { font-size: 46px; }
  .card--front .brand__tagline { font-size: 15px; padding-left: 50px; }

  .card--back .brand { left: 50%; top: 50%; transform: translate(-50%, -55%); text-align: center; }
  .card--back .brand__name { font-size: 64px; }
  .card--back .brand__tagline { font-size: 20px; }

  .holder {
    position: absolute;
    right: 44px;
    top: 118px;
    text-align: right;
  }
  .holder__name {
    color: var(--red);
    font-weight: 900;
    font-size: 30px;
    line-height: 1;
  }
  .holder__role {
    color: var(--grey-text);
    font-size: 15px;
    margin-top: 4px;
  }

  .contact {
    position: absolute;
    left: 48px;
    top: 222px;
    color: var(--grey-text);
    font-size: 14px;
    line-height: 1.3;
  }
  .contact__company { color: var(--red); font-weight: 700; font-size: 15px; }
  .contact__list { list-style: none; margin-top: 10px; }
  .contact__list li { display: flex; align-items: center; gap: 12px; height: 22px; }
  .contact__list svg { width: 14px; height: 14px; fill: none; stroke: var(--red); stroke-width: 1.8; }
</style>
</head>
<body>

  <section class="card card--front" aria-label="Anverso de la tarjeta">
    <div class="brand">
      <div class="brand__name">VALDORA</div>
      <div class="brand__tagline">MODA &amp; LENCERIA</div>
    </div>

    <div class="holder">
      <div class="holder__name">ANDRÉS VELA</div>
      <div class="holder__role">Founder &amp; Derector</div>
    </div>

    <div class="contact">
      <div class="contact__company">Valdora Moda &amp; Lencria</div>
      <div>P.O. Box 55555</div>
      <div>Your City&nbsp; Address Here</div>
      <ul class="contact__list">
        <li>
          <svg viewBox="0 0 16 16" aria-hidden="true"><path d="M3 2h3l1.5 3.5-2 1.2a8 8 0 0 0 3.8 3.8l1.2-2L14 10v3a1 1 0 0 1-1 1A11 11 0 0 1 2 3a1 1 0 0 1 1-1z"/></svg>
          0991234567
        </li>
        <li>
          <svg viewBox="0 0 16 16" aria-hidden="true"><rect x="1.5" y="3.5" width="13" height="9"/><path d="M1.5 3.5 8 9l6.5-5.5"/></svg>
          hola@valdora.ec
        </li>
        <li>
          <svg viewBox="0 0 16 16" aria-hidden="true"><circle cx="8" cy="8" r="6.5"/><path d="M1.5 8h13M8 1.5c-3 3.5-3 9.5 0 13M8 1.5c3 3.5 3 9.5 0 13"/></svg>
          www.valdora.ec
        </li>
      </ul>
    </div>
  </section>

  <section class="card card--back" aria-label="Reverso de la tarjeta">
    <div class="brand">
      <div class="brand__name">VALDORA</div>
      <div class="brand__tagline">MODA &amp; LENCERIA</div>
    </div>
  </section>

</body>
</html>
```